I need a design with just the number 24. must be in blue color (royal blue) should be large enough for people see must be in the center of page. Place a nice border around the page.

Requirements
Must have
• Number 24 in Royal blue color

```html
<!DOCTYPE html>
<html lang="en">
<head>
<meta charset="UTF-8">
<title>24</title>
<link rel="stylesheet" href="https://fonts.googleapis.com/css2?family=Archivo+Black&display=swap">
<style>
  :root {
    --royal-blue: #0023b5;
    --deep-blue: #001a78;
    --paper: #ffffff;
  }
  * { margin: 0; padding: 0; box-sizing: border-box; }
  html, body {
    width: 928px;
    height: 1200px;
    overflow: hidden;
    background: var(--paper);
  }
  .page-frame {
    position: relative;
    width: 928px;
    height: 1200px;
    background: var(--royal-blue);
    overflow: hidden;
  }
  .page-panel {
    position: absolute;
    left: 75px;
    top: 75px;
    width: 778px;
    height: 1050px;
    background: var(--paper);
    box-shadow: 0 0 34px 14px var(--deep-blue);
  }
  .number-art {
    position: absolute;
    inset: 0;
    width: 928px;
    height: 1200px;
  }
  .number-text {
    font-family: "Archivo Black", "Arial Black", sans-serif;
    font-size: 800px;
  }
  .number-shadow { fill: var(--deep-blue); }
  .number-face {
    fill: var(--royal-blue);
    stroke: var(--paper);
    stroke-width: 8px;
    stroke-linejoin: round;
    paint-order: stroke;
  }
</style>
</head>
<body>
  <div class="page-frame">
    <div class="page-panel"></div>
    <svg class="number-art" viewBox="0 0 928 1200" xmlns="http://www.w3.org/2000/svg" aria-label="24">
      <text class="number-text number-shadow" x="126" y="911" textLength="723" lengthAdjust="spacingAndGlyphs" aria-hidden="true">24</text>
      <text class="number-text number-face" x="107" y="892" textLength="723" lengthAdjust="spacingAndGlyphs">24</text>
    </svg>
  </div>
</body>
</html>
```